Pathways to Brightmoor Land Ventures

size of the ad - 8”x 10.75" plus 0.25" bleed
I would like an ad for a magazine that will stand out and make people want to read the ad.
The ad should not be crowded and people reading the ad will be able to read the text.
I would like it to be a creative and modern-day design.
the list of topics should not be the focus of the ad.
the text is attached.
If you decide to use people in the ad then please no ladies.
please note that leave over 1 inch for the bottom of the footer

```html
<!DOCTYPE html>
<html lang="en">
<head>
<meta charset="utf-8">
<title>Real Estate Course – Magazine Ad</title>
<link href="https://fonts.googleapis.com/css2?family=Montserrat:wght@500;600;700&display=swap" rel="stylesheet">
<style>
  :root {
    --orange: #f7931e;
    --black: #050505;
    --ink: #2b2b2b;
    --white: #ffffff;
    --stage: #ececec;
    --warm: #8a6b5c;
  }
  * { margin: 0; padding: 0; box-sizing: border-box; }
  html, body { width: 1200px; height: 2322px; overflow: hidden; background: var(--stage); }
  body { position: relative; font-family: "Montserrat", Arial, sans-serif; }

  .ad-frame {
    position: absolute; left: 50px; top: 421px;
    width: 935px; height: 1258px;
    transform: scale(1.1765); transform-origin: top left;
    background: var(--white); overflow: hidden;
  }
  .top-accent { position: absolute; left: 623px; top: 0; width: 233px; height: 92px; background: var(--orange); }

  .header-band {
    position: absolute; left: 0; top: 92px; width: 935px; height: 428px;
    background: var(--black);
  }
  .header-photo {
    position: absolute; left: 420px; top: 0; width: 515px; height: 428px;
    background: linear-gradient(90deg, rgba(5,5,5,1) 0%, rgba(60,45,40,0.9) 40%, var(--warm) 100%);
  }
  .course-title {
    position: absolute; left: 30px; top: 112px;
    font-size: 96px; font-weight: 500; line-height: 88px; color: var(--white); letter-spacing: -1px;
  }
  .course-title .accent { color: var(--orange); }

  .program-name {
    position: absolute; left: 32px; top: 311px; width: 365px; height: 175px;
    border-top: 3px solid var(--orange); border-left: 3px solid var(--orange);
    padding: 10px 0 0 12px;
    font-size: 40px; font-weight: 600; line-height: 39px; color: var(--white); text-transform: uppercase; white-space: nowrap;
  }
  .program-name .accent { color: var(--orange); }

  .tagline {
    position: absolute; left: 29px; top: 534px;
    font-size: 28px; font-weight: 600; line-height: 30px; color: var(--black);
  }

  .session-box {
    position: absolute; left: 0; top: 665px; width: 357px; height: 133px;
    background: var(--black); border-bottom-right-radius: 26px;
    padding: 6px 0 0 29px; color: var(--white);
  }
  .session-box .location { font-size: 36px; font-weight: 600; line-height: 40px; color: var(--orange); }
  .session-box .detail { font-size: 20px; font-weight: 600; line-height: 25px; }

  .early-bird { position: absolute; left: 29px; top: 808px; }
  .early-bird .label { font-size: 20px; font-weight: 600; color: var(--orange); line-height: 26px; }
  .early-bird .text { font-size: 20px; font-weight: 600; color: var(--black); line-height: 25px; margin-top: 4px; }

  .topics-heading {
    position: absolute; left: 29px; top: 904px;
    font-size: 36px; font-weight: 600; color: var(--ink); line-height: 44px;
  }
  .topics-heading .accent { color: var(--orange); }

  .topic-list { position: absolute; top: 956px; list-style: none; }
  .topic-list.first { left: 29px; }
  .topic-list.second { left: 402px; }
  .topic-list li {
    display: flex; align-items: center; gap: 8px;
    font-size: 20px; font-weight: 500; color: var(--ink); height: 28.5px;
  }
  .topic-list svg { width: 16px; height: 16px; flex: none; }

  .hex-art { position: absolute; left: 0; top: 0; width: 935px; height: 1258px; }

  .footer-band {
    position: absolute; left: 0; top: 1111px; width: 935px; height: 147px; background: var(--black);
    display: flex; flex-direction: column; align-items: center; justify-content: center; color: var(--white);
  }
  .footer-band .measure { font-size: 26px; font-weight: 500; line-height: 32px; }
  .footer-band svg { width: 14px; height: 30px; }
</style>
</head>
<body>
  <div class="ad-frame">
    <div class="top-accent"></div>

    <div class="header-band">
      <div class="header-photo" role="img" aria-label="Faded photo of a wooden house at dusk"></div>
    </div>

    <h1 class="course-title"><span class="accent">Real</span> Estate<br>Course</h1>

    <h2 class="program-name">
      <span class="accent">Pathways</span><br>To<br><span class="accent">Brightmoor</span><br>Land Ventures
    </h2>

    <svg class="hex-art" viewBox="0 0 935 1258">
      <defs>
        <linearGradient id="photo-night" x1="0" y1="0" x2="0" y2="1">
          <stop offset="0" stop-color="#6f8fa8"/>
          <stop offset="0.45" stop-color="#1a1a1a"/>
          <stop offset="0.75" stop-color="#3e5a2a"/>
          <stop offset="1" stop-color="#4a4a4a"/>
        </linearGradient>
        <linearGradient id="photo-day" x1="0" y1="0" x2="0" y2="1">
          <stop offset="0" stop-color="#8fb4dc"/>
          <stop offset="0.5" stop-color="#b08a5a"/>
          <stop offset="1" stop-color="#cfc6b8"/>
        </linearGradient>
        <linearGradient id="photo-blue" x1="0" y1="0" x2="0" y2="1">
          <stop offset="0" stop-color="#1f4fae"/>
          <stop offset="0.45" stop-color="#1c1c1c"/>
          <stop offset="0.75" stop-color="#b0764a"/>
          <stop offset="1" stop-color="#3a3a3a"/>
        </linearGradient>
      </defs>
      <g>
        <polygon points="677,208 900,336 900,590 677,718 454,590 454,336" fill="var(--white)" stroke="var(--orange)" stroke-width="12"/>
        <polygon transform="translate(677 463) scale(0.92) translate(-677 -463)" points="677,208 900,336 900,590 677,718 454,590 454,336" fill="url(#photo-night)" role="img" aria-label="Photo of a modern black house with lit windows at dusk"/>
      </g>
      <g>
        <polygon points="565,683 680,749 680,882 565,948 450,882 450,749" fill="var(--white)" stroke="var(--orange)" stroke-width="8"/>
        <polygon transform="translate(565 815) scale(0.9) translate(-565 -815)" points="565,683 680,749 680,882 565,948 450,882 450,749" fill="url(#photo-day)" role="img" aria-label="Photo of a modern timber-clad house"/>
      </g>
      <g>
        <polygon points="922,633 1130,740 1130,956 922,1063 714,956 714,740" fill="var(--white)" stroke="var(--orange)" stroke-width="10"/>
        <polygon transform="translate(922 848) scale(0.92) translate(-922 -848)" points="922,633 1130,740 1130,956 922,1063 714,956 714,740" fill="url(#photo-blue)" role="img" aria-label="Photo of a modern house with a lit entrance at twilight"/>
      </g>
    </svg>

    <p class="tagline">INVESTING<br>IN KNOWLEDGE<br>IS INVESTING<br>IN OPPORTUNITIES.</p>

    <div class="session-box">
      <p class="location">Harlowvale</p>
      <p class="detail">10 -Tuesday evenings sessions</p>
      <p class="detail">Starting Feb.28</p>
      <p class="detail">Limited Partial Scholarships</p>
    </div>

    <div class="early-bird">
      <p class="label">Early Bird Special</p>
      <p class="text">For those that started or<br>would like to go into real estate</p>
    </div>

    <h3 class="topics-heading"><span class="accent">Topics:</span> partial listing</h3>

    <ul class="topic-list first">
      <li><svg viewBox="0 0 16 16"><circle cx="8" cy="8" r="6.5" fill="none" stroke="var(--orange)" stroke-width="1.6"/><path d="M4.8 8.2l2.2 2.2 5-5.4" fill="none" stroke="var(--orange)" stroke-width="1.8"/></svg>Real estate investment strategies</li>
      <li><svg viewBox="0 0 16 16"><circle cx="8" cy="8" r="6.5" fill="none" stroke="var(--orange)" stroke-width="1.6"/><path d="M4.8 8.2l2.2 2.2 5-5.4" fill="none" stroke="var(--orange)" stroke-width="1.8"/></svg>Due diligence</li>
      <li><svg viewBox="0 0 16 16"><circle cx="8" cy="8" r="6.5" fill="none" stroke="var(--orange)" stroke-width="1.6"/><path d="M4.8 8.2l2.2 2.2 5-5.4" fill="none" stroke="var(--orange)" stroke-width="1.8"/></svg>Financing</li>
      <li><svg viewBox="0 0 16 16"><circle cx="8" cy="8" r="6.5" fill="none" stroke="var(--orange)" stroke-width="1.6"/><path d="M4.8 8.2l2.2 2.2 5-5.4" fill="none" stroke="var(--orange)" stroke-width="1.8"/></svg>Underwriting</li>
      <li><svg viewBox="0 0 16 16"><circle cx="8" cy="8" r="6.5" fill="none" stroke="var(--orange)" stroke-width="1.6"/><path d="M4.8 8.2l2.2 2.2 5-5.4" fill="none" stroke="var(--orange)" stroke-width="1.8"/></svg>Property management</li>
    </ul>
    <ul class="topic-list second">
      <li><svg viewBox="0 0 16 16"><circle cx="8" cy="8" r="6.5" fill="none" stroke="var(--orange)" stroke-width="1.6"/><path d="M4.8 8.2l2.2 2.2 5-5.4" fill="none" stroke="var(--orange)" stroke-width="1.8"/></svg>Real estate Legal basics</li>
      <li><svg viewBox="0 0 16 16"><circle cx="8" cy="8" r="6.5" fill="none" stroke="var(--orange)" stroke-width="1.6"/><path d="M4.8 8.2l2.2 2.2 5-5.4" fill="none" stroke="var(--orange)" stroke-width="1.8"/></svg>Sourcing deals</li>
      <li><svg viewBox="0 0 16 16"><circle cx="8" cy="8" r="6.5" fill="none" stroke="var(--orange)" stroke-width="1.6"/><path d="M4.8 8.2l2.2 2.2 5-5.4" fill="none" stroke="var(--orange)" stroke-width="1.8"/></svg>Syndication</li>
      <li><svg viewBox="0 0 16 16"><circle cx="8" cy="8" r="6.5" fill="none" stroke="var(--orange)" stroke-width="1.6"/><path d="M4.8 8.2l2.2 2.2 5-5.4" fill="none" stroke="var(--orange)" stroke-width="1.8"/></svg>Dealing with brokers</li>
      <li><svg viewBox="0 0 16 16"><circle cx="8" cy="8" r="6.5" fill="none" stroke="var(--orange)" stroke-width="1.6"/><path d="M4.8 8.2l2.2 2.2 5-5.4" fill="none" stroke="var(--orange)" stroke-width="1.8"/></svg>Tax fundamentals</li>
    </ul>

    <div class="footer-band">
      <svg viewBox="0 0 14 30"><path d="M7 29V3M2 9l5-7 5 7" fill="none" stroke="var(--white)" stroke-width="2"/></svg>
      <p class="measure">1.25”</p>
      <svg viewBox="0 0 14 30"><path d="M7 1v26M2 21l5 7 5-7" fill="none" stroke="var(--white)" stroke-width="2"/></svg>
    </div>
  </div>
</body>
</html>
```